Commercial construction contractor website.

We need a website that contains About Us, Contact info, Services, Project pictures and Industry News section

Target Market(s)

I'm building industral/flex spaces/commercial.

Industry/Entity Type

Commercial/industrial construction

Coding

Coded - Design and coding required

Number of Pages Required

5+ page

Font styles to use
Other font styles liked:
• The logo font is Microgramma Pro

Requirements
Must have
• Must have correct company name spelling: Halden Ridge Construction
Nice to have
• I do like to see our logo design implemented in the design
Should not have
• Please do not show big city pictures and business suit people. We are a commercial construction company

```html
<!DOCTYPE html>
<html lang="en">
<head>
<meta charset="utf-8">
<title>Halden Ridge Construction</title>
<link href="https://fonts.googleapis.com/css2?family=Poppins:wght@400;500;600&family=Rubik:wght@500;700&family=Michroma&display=swap" rel="stylesheet">
<style>
:root{
  --navy:#0c2d5c;
  --blue:#0a5aa8;
  --cyan:#1ba3dc;
  --grey-btn:#6a6a6a;
  --text:#4a4a4a;
  --light:#f2f2f2;
  --white:#ffffff;
}
*{margin:0;padding:0;box-sizing:border-box}
html,body{width:1200px;height:4680px;overflow:hidden}
body{position:relative;background:var(--white);font-family:"Poppins",sans-serif;color:var(--text)}
.abs{position:absolute}
.label{font-family:"Michroma",sans-serif;font-size:12px;letter-spacing:1.5px;color:#555;text-transform:uppercase;white-space:nowrap}
.heading{font-family:"Rubik",sans-serif;font-weight:700;color:var(--navy);text-transform:uppercase;line-height:1;white-space:nowrap}
.center{left:0;width:1200px;text-align:center}
.para{font-size:12.5px;line-height:20px;color:var(--text)}
.btn{position:absolute;background:var(--grey-btn);color:var(--white);font-family:"Michroma",sans-serif;font-size:10px;letter-spacing:.5px;white-space:nowrap;display:flex;align-items:center;padding-left:12px;text-transform:uppercase}
.btn::after{content:"";position:absolute;right:-14px;top:0;width:5px;height:100%;background:var(--grey-btn);transform:skewX(-22deg)}
.btn::before{content:"";position:absolute;right:-4px;top:0;width:10px;height:100%;background:var(--white);transform:skewX(-22deg)}

/* top bar & nav */
.topbar{top:0;left:0;width:1200px;height:36px;background:linear-gradient(90deg,#0b3f7e,var(--navy) 60%,#0d3d76)}
.topbar .item{position:absolute;top:0;height:36px;display:flex;align-items:center;gap:12px;color:var(--white);font-size:12px;white-space:nowrap}
.nav{top:36px;left:0;width:1200px;height:55px;background:var(--white)}
.nav a{position:absolute;top:19px;font-size:12px;color:#555;text-decoration:none;white-space:nowrap}
.nav a.active{color:var(--blue)}
.nav .dot{position:absolute;left:633px;top:40px;width:10px;height:10px;border-radius:50%;border:2px solid var(--blue)}
.brand-tab{top:36px;left:0;width:236px;height:97px;background:var(--white);clip-path:polygon(0 0,210px 0,236px 40px,214px 97px,0 97px);z-index:3;display:flex;align-items:center;justify-content:center}
.brand-name{font-family:"Michroma",sans-serif;font-size:11px;color:var(--navy);text-align:center;line-height:16px;letter-spacing:.5px}

/* hero */
.hero{top:91px;left:0;width:1200px;height:740px}
.hero-photo{position:absolute;inset:0;clip-path:polygon(0 0,1200px 0,1200px 555px,600px 736px,100px 640px,0 473px);background:linear-gradient(120deg,#2a3b52 0%,#3a5574 35%,#8a6a3a 62%,#3b5270 85%,#22344c 100%)}
.hero-title{left:60px;top:192px;font-family:"Rubik",sans-serif;font-weight:700;font-size:58px;line-height:64px;color:var(--white);white-space:nowrap}
.hero-title .accent{color:var(--cyan)}
.hero-text{left:61px;top:333px;width:380px;color:var(--white);font-size:12px;line-height:19px}

/* about */
.about-photo{left:620px;top:905px;width:455px;height:400px;background:linear-gradient(160deg,#3d7fc4,#0b4e95 55%,#0a3570)}
.ticks{left:113px;top:1066px;width:340px;list-style:none}
.ticks li{position:relative;padding-left:30px;font-size:12px;line-height:20px;margin-bottom:5px}
.ticks li::before{content:"";position:absolute;left:0;top:3px;width:14px;height:14px;border:2px solid var(--blue);border-radius:3px;background:var(--white)}

/* services */
.service{position:absolute;width:300px;text-align:center}
.service .hex-frame{margin:0 auto;width:273px;height:215px;background:#8a8a8a;clip-path:polygon(25% 0,75% 0,100% 50%,75% 100%,25% 100%,0 50%);display:flex;align-items:center;justify-content:center}
.service .hex-frame.featured{background:var(--blue)}
.service .hex-img{width:263px;height:205px;clip-path:polygon(25% 0,75% 0,100% 50%,75% 100%,25% 100%,0 50%)}
.service h3{font-size:14px;font-weight:500;color:#222;margin-top:14px}
.service p{font-size:12px;line-height:19px;margin-top:12px;padding:0 25px}

/* projects */
.project{position:absolute;width:287px;height:313px;clip-path:polygon(50% 0,100% 25%,100% 75%,50% 100%,0 75%,0 25%)}
.project-overlay{position:absolute;inset:0;background:rgba(20,110,200,.72);display:flex;flex-direction:column;align-items:center;justify-content:center;color:var(--white);font-size:14px;font-weight:500}
.project-overlay span{font-size:30px;font-weight:300;line-height:30px;margin-top:4px}

/* contact */
.info{position:absolute;top:3180px;display:flex;align-items:center;gap:14px;white-space:nowrap}
.info .ico{width:46px;height:52px}
.info b{display:block;font-size:12px;font-weight:500;color:var(--navy)}
.info small{font-size:11px;color:#555}
.field{position:absolute;background:var(--white);border:1px solid #cfcfcf;font-size:11.5px;color:#444;padding:8px 10px}
.field.focus{border-color:var(--blue)}

/* news */
.card{position:absolute;top:3756px;width:272px;height:417px;background:var(--white);box-shadow:0 2px 10px rgba(0,0,0,.08)}
.card .photo{height:211px}
.card .date{position:absolute;left:200px;top:188px;width:48px;height:54px;background:var(--navy);clip-path:polygon(50% 0,100% 25%,100% 75%,50% 100%,0 75%,0 25%);color:var(--white);font-size:13px;font-weight:500;text-align:center;line-height:15px;padding-top:12px}
.card h4{position:absolute;left:17px;top:260px;width:240px;font-size:12px;font-weight:600;color:#222;line-height:20px}
.card p{position:absolute;left:17px;top:310px;width:240px;font-size:11.5px;line-height:21px;color:#777}

/* footer */
.footer-title{position:absolute;top:4414px;font-size:14px;color:var(--cyan);font-weight:500}
.sitemap{position:absolute;left:337px;top:4444px;list-style:none}
.sitemap li{color:#e2ecf7;font-size:12px;line-height:30px}
.fcontact{position:absolute;left:610px;display:flex;align-items:center;gap:14px;color:var(--white);font-size:12px;white-space:nowrap}
.copyright{top:4647px;left:0;width:1200px;height:33px;background:var(--blue);color:var(--white);font-size:11.5px;text-align:center;line-height:33px}
</style>
</head>
<body>

<!-- top bar -->
<div class="abs topbar">
  <div class="item" style="left:460px">
    <svg width="16" height="18" viewBox="0 0 16 18"><path d="M8 1a6 6 0 0 0-6 6c0 4.5 6 10 6 10s6-5.5 6-10a6 6 0 0 0-6-6z" fill="none" stroke="#fff" stroke-width="1.4"/><circle cx="8" cy="7" r="2.2" fill="none" stroke="#fff" stroke-width="1.4"/></svg>
    101-Lorem ipsum is dummy</div>
  <div class="item" style="left:764px">
    <svg width="16" height="16" viewBox="0 0 16 16"><path d="M3 1.5l3 .5 1 3.5-2 1.5a9 9 0 0 0 4.5 4.5l1.5-2 3.5 1 .5 3c-7 1-13-5-12-12z" fill="none" stroke="#fff" stroke-width="1.3"/></svg>
    123 456 7890</div>
  <div class="item" style="left:958px">
    <svg width="18" height="14" viewBox="0 0 18 14"><rect x="1" y="1" width="16" height="12" fill="none" stroke="#fff" stroke-width="1.3"/><path d="M1 1l8 7 8-7" fill="none" stroke="#fff" stroke-width="1.3"/></svg>
    info@haldenridge.com</div>
</div>

<!-- nav -->
<div class="abs nav">
  <a class="active" style="left:624px">Home</a>
  <span class="dot"></span>
  <a style="left:691px">About Us</a>
  <a style="left:777px">Services</a>
  <a style="left:860px">Project</a>
  <a style="left:935px">News</a>
  <div class="btn" style="left:996px;top:9px;width:122px;height:37px">Contact Us</div>
</div>
<div class="abs brand-tab"><div class="brand-name">HALDEN RIDGE<br>CONSTRUCTION</div></div>

<!-- hero -->
<div class="abs hero">
  <div class="hero-photo" role="img" aria-label="Construction workers in hard hats reviewing plans on site"></div>
  <svg class="abs" style="left:0;top:0" width="1200" height="740"><polyline points="0,473 100,640 600,736 1200,555" fill="none" stroke="#0a5aa8" stroke-width="5"/></svg>
  <div class="abs hero-title"><span class="accent">WE BUILD</span> YOUR<br>DREAM</div>
  <p class="abs hero-text">Lorem Ipsum is simply dummy text of the printing and typesetting industry. Lorem Ipsum has been the industry's standard dummy text ever since the 1500s,</p>
  <div class="btn" style="left:60px;top:411px;width:120px;height:36px">Contact Us</div>
</div>

<!-- about -->
<div class="abs label" style="left:115px;top:908px">Halden Ridge Construction</div>
<div class="abs heading" style="left:113px;top:940px;font-size:46px">About Us</div>
<p class="abs para" style="left:114px;top:987px;width:430px;font-size:12px">Lorem Ipsum is simply dummy text of the printing and typesetting industry. Lorem Ipsum has been the industry's standard dummy text ever since the 1500s,</p>
<ul class="abs ticks">
  <li>Lorem Ipsum is simply dummy text of the printing and typesetting industry.</li>
  <li>Lorem Ipsum is simply dummy text of the printing and typesetting industry.</li>
  <li>Lorem Ipsum is simply dummy text of the printing and typesetting industry.</li>
  <li>Lorem Ipsum is simply dummy text of the printing and typesetting industry.</li>
</ul>
<div class="btn" style="left:113px;top:1267px;width:120px;height:36px">Contact Us</div>
<div class="abs about-photo" role="img" aria-label="Blue-toned photo of a building under construction"></div>

<!-- services -->
<svg class="abs" style="left:0;top:1380px" width="1200" height="800">
  <defs><linearGradient id="edge" x1="0" x2="1"><stop offset="0" stop-color="#0c2d5c"/><stop offset="1" stop-color="#1ba3dc"/></linearGradient></defs>
  <polygon points="600,11 1200,213 1200,520 1100,693 600,793 100,652 0,592 0,274 100,114" fill="#f2f2f2"/>
  <polyline points="0,274 100,114 600,11 1200,213" fill="none" stroke="url(#edge)" stroke-width="5"/>
  <polyline points="0,592 100,652 600,793 1100,693 1200,520" fill="none" stroke="url(#edge)" stroke-width="5"/>
</svg>
<div class="abs label center" style="top:1494px">What we do</div>
<div class="abs heading center" style="top:1524px;font-size:44px">Services</div>
<p class="abs para center" style="top:1576px;padding:0 395px;font-size:12px">Lorem Ipsum is simply dummy text of the printing and typesetting industry. Lorem Ipsum has been the industry's</p>
<div class="service" style="left:103px;top:1669px">
  <div class="hex-frame"><div class="hex-img" role="img" aria-label="Modern commercial interior with staircase" style="background:linear-gradient(135deg,#b88a5a,#6f4f36 60%,#d9b27a)"></div></div>
  <h3>Commercial Design</h3>
  <p>Lorem Ipsum is simply dummy text of the printing and typesetting industry. Lorem Ipsum has been the industry's</p>
</div>
<div class="service" style="left:459px;top:1641px">
  <div class="hex-frame featured"><div class="hex-img" role="img" aria-label="Building model on construction blueprints" style="background:linear-gradient(135deg,#e8e8ec,#b9a07c 50%,#d6dbe2)"></div></div>
  <h3 style="margin-top:42px">Development construction</h3>
  <p>Lorem Ipsum is simply dummy text of the printing and typesetting industry. Lorem Ipsum has been the industry's</p>
</div>
<div class="service" style="left:805px;top:1669px">
  <div class="hex-frame"><div class="hex-img" role="img" aria-label="Workers planning a renovation in an empty room" style="background:linear-gradient(135deg,#dcd9d4,#9a958e 55%,#c8c3bb)"></div></div>
  <h3>Renovation</h3>
  <p>Lorem Ipsum is simply dummy text of the printing and typesetting industry. Lorem Ipsum has been the industry's</p>
</div>

<!-- projects -->
<div class="abs label center" style="top:2238px">Our work</div>
<div class="abs heading center" style="top:2267px;font-size:44px">Our Project</div>
<div class="project" style="left:142px;top:2331px;background:linear-gradient(135deg,#c9b59a,#8c6f52 55%,#e4ddd2)" role="img" aria-label="Finished living room interior"></div>
<div class="project" style="left:457px;top:2331px;background:linear-gradient(135deg,#2b5f94,#1d4770)" role="img" aria-label="Construction team on site">
  <div class="project-overlay">Development construction<span>+</span></div>
</div>
<div class="project" style="left:772px;top:2331px;background:linear-gradient(135deg,#6b4c33,#d48a45 50%,#3a2a1f)" role="img" aria-label="Glass-fronted commercial building lit at dusk"></div>
<div class="project" style="left:299px;top:2609px;background:linear-gradient(135deg,#e6e2db,#3f3a35 60%,#a9865a)" role="img" aria-label="Kitchen interior with pendant lights"></div>
<div class="project" style="left:614px;top:2609px;background:linear-gradient(135deg,#a77a50,#e7ddd0 50%,#6d4e35)" role="img" aria-label="Office interior with wood slat ceiling"></div>

<!-- contact -->
<svg class="abs" style="left:0;top:2960px" width="1200" height="640">
  <polygon points="600,9 1000,80 1200,276 1200,420 1100,560 600,625 100,522 0,367 0,220 100,113" fill="#f2f2f2"/>
  <polyline points="100,113 600,9 1000,80 1200,276" fill="none" stroke="url(#edge)" stroke-width="5"/>
  <polyline points="0,367 100,522 600,625 1100,560 1200,420" fill="none" stroke="url(#edge)" stroke-width="5"/>
</svg>
<div class="abs label center" style="top:3059px">Get in touch</div>
<div class="abs heading center" style="top:3080px;font-size:44px">Contact Us</div>

<div class="info" style="left:197px">
  <svg class="ico" viewBox="0 0 46 52"><polygon points="23,2 44,14 44,38 23,50 2,38 2,14" fill="none" stroke="#0a5aa8" stroke-width="2"/><rect x="14" y="19" width="18" height="14" fill="none" stroke="#0a5aa8" stroke-width="2"/><path d="M14 19l9 7 9-7" fill="none" stroke="#0a5aa8" stroke-width="2"/></svg>
  <div><b>24 X 7 online support</b><small>info@haldenridge.com</small></div>
</div>
<div class="info" style="left:475px">
  <svg class="ico" viewBox="0 0 46 52"><polygon points="23,2 44,14 44,38 23,50 2,38 2,14" fill="none" stroke="#0a5aa8" stroke-width="2"/><path d="M15 16l4 .5 1.5 4.5-2.5 2a11 11 0 0 0 6 6l2-2.5 4.5 1.5.5 4c-9 1.5-17-6.5-16-16z" fill="none" stroke="#0a5aa8" stroke-width="2"/></svg>
  <div><b>Contact Us Free</b><small>123 456 7890</small></div>
</div>
<div class="info" style="left:723px">
  <svg class="ico" viewBox="0 0 46 52"><polygon points="23,2 44,14 44,38 23,50 2,38 2,14" fill="none" stroke="#0a5aa8" stroke-width="2"/><path d="M23 15a6 6 0 0 0-6 6c0 4.5 6 11 6 11s6-6.5 6-11a6 6 0 0 0-6-6z" fill="none" stroke="#0a5aa8" stroke-width="2"/><circle cx="23" cy="21" r="2" fill="#0a5aa8"/></svg>
  <div><b>Office Address</b><small>101 - Lorem ipsum is printing dummy</small></div>
</div>

<div class="field focus" style="left:287px;top:3273px;width:286px;height:36px">Name *</div>
<div class="field" style="left:287px;top:3318px;width:286px;height:36px">Email *</div>
<div class="field" style="left:287px;top:3364px;width:286px;height:36px">Address *</div>
<div class="field" style="left:589px;top:3273px;width:284px;height:127px">Message *</div>
<div class="btn" style="left:427px;top:3423px;width:126px;height:37px">Submit Now</div>
<div class="btn" style="left:593px;top:3423px;width:124px;height:37px">Get a Quote</div>

<!-- news -->
<div class="abs label center" style="top:3656px">Blog</div>
<div class="abs heading center" style="top:3686px;font-size:44px">Latest News</div>

<div class="card" style="left:164px">
  <div class="photo" role="img" aria-label="Two site workers in safety vests and hard hats" style="background:linear-gradient(135deg,#8fb4d6,#6fae3c 55%,#3b6f2a)"></div>
  <div class="date">6<br>Jan</div>
  <h4>Lorem Ipsum is simply dummy text of the printing and typesetting.</h4>
  <p>Lorem Ipsum is simply dummy text of the printing and typesetting industry. Lorem Ipsum has been the industry's</p>
</div>
<div class="card" style="left:465px">
  <div class="photo" role="img" aria-label="Hands working over construction drawings with tools" style="background:linear-gradient(135deg,#c7a072,#e9e2d6 50%,#9b7a55)"></div>
  <div class="date">6<br>Jan</div>
  <h4>Lorem Ipsum is simply dummy text of the printing and typesetting.</h4>
  <p>Lorem Ipsum is simply dummy text of the printing and typesetting industry. Lorem Ipsum has been the industry's</p>
</div>
<div class="card" style="left:764px">
  <div class="photo" role="img" aria-label="Builders measuring timber indoors" style="background:linear-gradient(135deg,#d5cfc6,#6e7f99 55%,#b7ab98)"></div>
  <div class="date">6<br>Jan</div>
  <h4>Lorem Ipsum is simply dummy text of the printing and typesetting.</h4>
  <p>Lorem Ipsum is simply dummy text of the printing and typesetting industry. Lorem Ipsum has been the industry's</p>
</div>

<!-- footer -->
<svg class="abs" style="left:0;top:4250px" width="1200" height="400">
  <defs><linearGradient id="foot" x1="0" y1="0" x2="1" y2="1"><stop offset="0" stop-color="#0c2d5c"/><stop offset="1" stop-color="#0b4a8f"/></linearGradient></defs>
  <polygon points="0,186 100,104 600,4 1200,104 1200,400 0,400" fill="url(#foot)"/>
  <polyline points="0,186 100,104 600,4 1200,104" fill="none" stroke="#0a5aa8" stroke-width="5"/>
</svg>
<div class="abs brand-name" style="left:48px;top:4505px;width:240px;color:#fff;font-size:15px;line-height:22px">HALDEN RIDGE<br>CONSTRUCTION</div>

<div class="footer-title" style="left:336px">Site Map</div>
<ul class="sitemap">
  <li>- Home</li><li>- About Us</li><li>- Services</li><li>- Project</li><li>- Contact Us</li>
</ul>

<div class="footer-title" style="left:612px">Contact Us</div>
<div class="fcontact" style="top:4442px">
  <svg width="34" height="38" viewBox="0 0 34 38"><polygon points="17,1 33,10 33,28 17,37 1,28 1,10" fill="none" stroke="#fff" stroke-width="1.5"/><path d="M17 11a5 5 0 0 0-5 5c0 3.5 5 9 5 9s5-5.5 5-9a5 5 0 0 0-5-5z" fill="none" stroke="#fff" stroke-width="1.5"/></svg>
  101-Lorem ipsum is dummy</div>
<div class="fcontact" style="top:4495px">
  <svg width="34" height="38" viewBox="0 0 34 38"><polygon points="17,1 33,10 33,28 17,37 1,28 1,10" fill="none" stroke="#fff" stroke-width="1.5"/><path d="M11 12l3 .5 1 3-2 1.5a8 8 0 0 0 4 4l1.5-2 3 1 .5 3c-6.5 1-12-4.5-11-11z" fill="none" stroke="#fff" stroke-width="1.5"/></svg>
  123 456 7890</div>
<div class="fcontact" style="top:4548px">
  <svg width="34" height="38" viewBox="0 0 34 38"><polygon points="17,1 33,10 33,28 17,37 1,28 1,10" fill="none" stroke="#fff" stroke-width="1.5"/><rect x="10" y="14" width="14" height="10" fill="none" stroke="#fff" stroke-width="1.5"/><path d="M10 14l7 5 7-5" fill="none" stroke="#fff" stroke-width="1.5"/></svg>
  info@haldenridge.com</div>

<div class="footer-title" style="left:889px">Newsletters</div>
<div class="field" style="left:887px;top:4443px;width:247px;height:35px;border:none;color:#777;font-size:11px">ENter Email Address.....</div>
<div class="btn" style="left:887px;top:4498px;width:124px;height:35px">Contact Us</div>

<div class="abs copyright">Copyright © HALDEN RIDGE 2022 All Rights Reserved.</div>

</body>
</html>
```